**Designs Wanted for High Profile Banner Ad Campaign**

Our leading Public Relations agency services some of the world's leading brands in our local market.

We now need a banner ad design to support our own growth.

We are looking to have banner ads designed that will carry a common theme to be used across the following sizes (all these sizes will need to be created):
• Vertical rectangle: 240 x 400
• Mobile leaderboard: 320 x 50
• Banner: 468 x 60
• Leaderboard: 728 x 90
• Square: 250 x 250
• Small square: 200 x 200
• Large rectangle: 336 x 280
• Inline rectangle: 300 x 250
• Skyscraper: 120 x 600
• Wide skyscraper: 160 x 600
• Half-page: 300 x 600
• Large leaderboard: 970x90
• Large mobile banner: 320 x 100
• Billboard: 970 x 250

Our primary retargeting and regular display campaign objective is to encourage marketing managers and business owners to visit our site and contact us.
See www.lumenvoicecomms.co.nz for our current look and feel. Please keep consistent colours with that site. Our two logos are attached.

This is our first digital retargeting campaign and we are open to your advice and suggestions on what will encourage click through from potential clients.

Our current thinking at the moment is that the ad could be built around these concepts:
“Reach, socialise, inspire.”
In others words – as a PR agency we help clients ‘reach’ their target market through creating content for news media.
The ‘socialise’ represents engagement through social media – in that we help develop and build their social media presence.
‘Inspire’ refers to the fact we aim to inspire their target market towards engaging with our clients.
Plus a suitable call to action– eg. Click here to meet your public relations needs today.

In terms of designs we are open to suggestion: eg. the adverts could use icons or something else that you have seen work.

We would like to see some eye catching animation, interaction or movement in the advert to.

We need the ad to be effective, eye catching, professional, modern, sophisticated (in that our target market is professional executives) and crisp, clean and uncluttered.

Time is short for us, so please send through designs as soon as possible – don’t wait until the last day!

Additional note: the existing fish image and 'stand out from the crowd' slogan on our home page are not required as part of this design. We have been looking to move towards the new slogan (“Reach, socialise, inspire.” ) and this banner ad may also serve to give us some new direction ideas as well. we do need to keep the existing logo and orange colour though.

Target Market(s)

Business to Business. Marketing and brand managers, Small, Medium and large business owners and executives.
Those with a business in the New Zealand market.

Industry/Entity Type

Marketing

Requirements
Must have
• our logo
animation or movement
orange colour/ consistency with our existing website.
our proposed slogan: “Reach, socialise, inspire.” (however we are open to seeing alternative ideas as well if you want to submit more than one concept)
call to action.
Should not have
• read note about existing fish and slogan above.

```html
<!DOCTYPE html>
<html lang="en">
<head>
<meta charset="utf-8">
<title>Lumen Voice – Banner Ad Set</title>
<link rel="stylesheet" href="https://fonts.googleapis.com/css2?family=Jost:wght@300;400;600&display=swap">
<style>
  :root {
    --stage: #e5e6e8;
    --orange: #ff6600;
    --white: #ffffff;
    --ink: #3a3a3a;
    --shadow: rgba(0, 0, 0, 0.28);
  }
  * { box-sizing: border-box; margin: 0; padding: 0; }
  html, body {
    width: 1200px; height: 760px; overflow: hidden;
    background: var(--stage);
    font-family: "Jost", "Century Gothic", sans-serif;
    color: var(--white);
  }
  .canvas { position: relative; width: 1200px; height: 760px; }

  .ad {
    position: absolute;
    background: var(--orange);
    border: 1px solid var(--orange);
    overflow: hidden;
  }
  .ad > * { position: absolute; }
  .logo-box { background: var(--white); display: flex; align-items: center; justify-content: center; }
  .wordmark { color: var(--ink); font-weight: 300; line-height: 1; letter-spacing: 1px; }
  .wordmark.stacked { text-align: center; }
  .wordmark.stacked span { display: block; }

  .slogan { font-weight: 400; letter-spacing: 0.5px; }
  .needs { font-weight: 400; }
  .needs strong { font-weight: 600; letter-spacing: 1px; }
  .signal { fill: none; stroke: var(--white); stroke-linecap: round; }
  .signal circle { fill: var(--white); stroke: none; }

  .cta-pill, .cta-round {
    background: var(--white);
    color: var(--orange);
    font-weight: 600;
    text-align: center;
    box-shadow: 0 2px 4px var(--shadow);
    display: flex; align-items: center; justify-content: center;
  }
  .cta-pill { border-radius: 8px; letter-spacing: 0.5px; }
  .cta-round { border-radius: 50%; line-height: 1.1; letter-spacing: 0.5px; }

  /* Square */
  .ad-square { left: 62px; top: 102px; width: 265px; height: 265px; }
  .ad-square .logo-box { left: 0; top: 0; width: 100%; height: 48px; }
  .ad-square .wordmark { font-size: 29px; }
  .ad-square .slogan { left: 19px; top: 60px; font-size: 25px; line-height: 28px; }
  .ad-square .signal { left: 171px; top: 84px; width: 76px; height: 54px; }
  .ad-square .needs { left: 19px; top: 155px; font-size: 15px; line-height: 18.5px; }
  .ad-square .cta-pill { left: 21px; top: 224px; width: 87px; height: 29px; font-size: 13px; }

  /* Mobile leaderboard */
  .ad-mobile { left: 62px; top: 395px; width: 339px; height: 53px; }
  .ad-mobile .logo-box { left: 0; top: 0; width: 63px; height: 100%; }
  .ad-mobile .wordmark { font-size: 10px; }
  .ad-mobile .wordmark span + span { font-size: 13px; margin-top: 2px; }
  .ad-mobile .slogan { left: 72px; top: 3px; font-size: 12.5px; line-height: 15px; letter-spacing: 1px; }
  .ad-mobile .signal { left: 157px; top: 10px; width: 48px; height: 33px; }
  .ad-mobile .needs { left: 216px; top: 6px; font-size: 11px; line-height: 13.5px; }

  /* Banner */
  .ad-banner { left: 62px; top: 472px; width: 495px; height: 63px; }
  .ad-banner .logo-box { left: 0; top: 0; width: 70px; height: 100%; }
  .ad-banner .wordmark { font-size: 11px; }
  .ad-banner .wordmark span + span { font-size: 15px; margin-top: 3px; }
  .ad-banner .slogan { left: 85px; top: 5px; font-size: 14px; line-height: 17px; letter-spacing: 1.5px; }
  .ad-banner .signal { left: 189px; top: 12px; width: 50px; height: 38px; }
  .ad-banner .needs { left: 259px; top: 7px; font-size: 14px; line-height: 16.5px; }
  .ad-banner .cta-round { left: 417px; top: 7px; width: 48px; height: 48px; font-size: 9.5px; }

  /* Leaderboard */
  .ad-leader { left: 62px; top: 564px; width: 770px; height: 95px; }
  .ad-leader .logo-box { left: 0; top: 0; width: 111px; height: 100%; }
  .ad-leader .wordmark { font-size: 17px; }
  .ad-leader .wordmark span + span { font-size: 23px; margin-top: 5px; }
  .ad-leader .slogan { left: 136px; top: 6px; font-size: 22px; line-height: 27px; letter-spacing: 2.5px; }
  .ad-leader .signal { left: 299px; top: 20px; width: 72px; height: 54px; }
  .ad-leader .needs { left: 403px; top: 6px; font-size: 22px; line-height: 27px; letter-spacing: 1px; }
  .ad-leader .cta-round { left: 667px; top: 9px; width: 76px; height: 76px; font-size: 15px; }

  /* Vertical rectangle */
  .ad-vertical { left: 883px; top: 236px; width: 254px; height: 423px; }
  .ad-vertical .logo-box { left: 0; top: 0; width: 100%; height: 59px; }
  .ad-vertical .wordmark { font-size: 29px; }
  .ad-vertical .slogan { left: 18px; top: 73px; font-size: 29px; line-height: 37px; }
  .ad-vertical .signal { left: 19px; top: 201px; width: 118px; height: 84px; }
  .ad-vertical .needs { left: 18px; top: 302px; font-size: 16px; line-height: 19.5px; }
  .ad-vertical .cta-pill { left: 65px; top: 375px; width: 118px; height: 31px; font-size: 17px; }
</style>
</head>
<body>
<main class="canvas">

  <svg width="0" height="0" style="position:absolute">
    <defs>
      <symbol id="signal-icon" viewBox="0 0 80 60">
        <circle cx="40" cy="30" r="6.5"/>
        <path d="M29 17 A17 17 0 0 0 29 43"/>
        <path d="M51 17 A17 17 0 0 1 51 43"/>
        <path d="M19 7 A31 31 0 0 0 19 53"/>
        <path d="M61 7 A31 31 0 0 1 61 53"/>
      </symbol>
    </defs>
  </svg>

  <section class="ad ad-square" aria-label="Square banner">
    <div class="logo-box"><span class="wordmark">LUMENVOICE</span></div>
    <p class="slogan">Reach,<br>socialise,<br>inspire.</p>
    <svg class="signal" stroke-width="5.5" aria-hidden="true"><use href="#signal-icon"/></svg>
    <p class="needs">Meet Your<br><strong>PUBLIC RELATIONS</strong><br>Needs Today</p>
    <div class="cta-pill">Click Here</div>
  </section>

  <section class="ad ad-mobile" aria-label="Mobile leaderboard">
    <div class="logo-box"><span class="wordmark stacked"><span>LUMEN</span><span>VOICE</span></span></div>
    <p class="slogan">Reach,<br>socialise,<br>inspire.</p>
    <svg class="signal" stroke-width="6" aria-hidden="true"><use href="#signal-icon"/></svg>
    <p class="needs">Meet Your<br><strong>PUBLIC RELATIONS</strong><br>Needs Today</p>
  </section>

  <section class="ad ad-banner" aria-label="Banner">
    <div class="logo-box"><span class="wordmark stacked"><span>LUMEN</span><span>VOICE</span></span></div>
    <p class="slogan">Reach,<br>socialise,<br>inspire.</p>
    <svg class="signal" stroke-width="6" aria-hidden="true"><use href="#signal-icon"/></svg>
    <p class="needs">Meet Your<br><strong>PUBLIC RELATIONS</strong><br>Needs Today</p>
    <div class="cta-round">CLICK<br>HERE</div>
  </section>

  <section class="ad ad-leader" aria-label="Leaderboard">
    <div class="logo-box"><span class="wordmark stacked"><span>LUMEN</span><span>VOICE</span></span></div>
    <p class="slogan">Reach,<br>socialise,<br>inspire.</p>
    <svg class="signal" stroke-width="5.5" aria-hidden="true"><use href="#signal-icon"/></svg>
    <p class="needs">Meet Your<br><strong>PUBLIC RELATIONS</strong><br>Needs Today</p>
    <div class="cta-round">CLICK<br>HERE</div>
  </section>

  <section class="ad ad-vertical" aria-label="Vertical rectangle">
    <div class="logo-box"><span class="wordmark">LUMENVOICE</span></div>
    <p class="slogan">Reach,<br>socialise,<br>inspire.</p>
    <svg class="signal" stroke-width="5" aria-hidden="true"><use href="#signal-icon"/></svg>
    <p class="needs">Meet Your<br><strong>PUBLIC RELATIONS</strong> Needs<br>Today</p>
    <div class="cta-pill">Click Here</div>
  </section>

</main>
</body>
</html>
```